Looking for a contemporary business card design with our logo

would like to consider a embossing look although I'm not married to the idea. We are a custom jeweler that needs a look that represents old world craftsmanship with a modern twist that's why we went with a more modern shield type of logo that can be stamped inside our rings.
It could be two sided or one we are more after a look the pops and is trendy and creative. (WE ARE NOT LOOKING FOR A COOKIE CUTTER LAYOUT)
We have attached the image and will be using the logo with harwick studio wording in the format that it's in unless you see a better way of doing it.
If the logo needs a twist we are O.K. with suggestions as well.
This card should scream "Quality" from a high end studio.
Harwick Studio
4186 Maplecrest Rd. Unit B-2
Windsor, CO 80317
www.harwickstudio-example.com
lu@harwickstudio-example.com
Should speak quality craftsmanship

```html
<!DOCTYPE html>
<html lang="en">
<head>
<meta charset="utf-8">
<title>Harwick Studio – Business Card</title>
<link rel="stylesheet" href="https://fonts.googleapis.com/css2?family=Arimo:ital,wght@0,400;0,700;1,400&display=swap">
<style>
  :root {
    --card-black: #000000;
    --panel-light: #8c8c8c;
    --panel-mid: #6a6a6a;
    --panel-dark: #3a3a3a;
    --mark-grey: #5c5c5c;
    --ink: #0d0d0d;
  }
  html, body {
    margin: 0;
    padding: 0;
    overflow: hidden;
    background: #ffffff;
  }
  .card {
    position: relative;
    width: 700px;
    height: 1200px;
    background: var(--card-black);
    overflow: hidden;
    font-family: "Arimo", Arial, sans-serif;
  }
  .diagonal-panel {
    position: absolute;
    inset: 0;
    width: 700px;
    height: 1200px;
  }
  .brand {
    position: absolute;
    left: 60px;
    top: 60px;
    display: flex;
    align-items: center;
    gap: 34px;
  }
  .brand-square {
    width: 200px;
    height: 200px;
    background: var(--mark-grey);
  }
  .brand-name {
    color: var(--mark-grey);
    font-weight: 700;
    font-size: 44px;
    line-height: 1.1;
  }
  .contact {
    position: absolute;
    right: 40px;
    top: 845px;
    text-align: right;
    color: var(--ink);
  }
  .contact-name {
    margin: 0 0 14px;
    font-size: 48px;
    font-weight: 700;
    letter-spacing: 0.5px;
  }
  .contact-address {
    margin: 0 0 10px;
    font-size: 37px;
    line-height: 1.2;
    font-style: normal;
  }
  .contact-web {
    margin: 0;
    font-size: 36px;
    line-height: 1.25;
    font-style: italic;
  }
</style>
</head>
<body>
  <div class="card">
    <svg class="diagonal-panel" viewBox="0 0 700 1200" aria-hidden="true">
      <defs>
        <linearGradient id="panelShade" x1="1" y1="0" x2="0" y2="1">
          <stop offset="0" stop-color="var(--panel-light)"/>
          <stop offset="0.5" stop-color="var(--panel-mid)"/>
          <stop offset="1" stop-color="var(--panel-dark)"/>
        </linearGradient>
      </defs>
      <polygon points="0,935 700,385 700,1200 0,1200" fill="url(#panelShade)"/>
    </svg>

    <div class="brand">
      <div class="brand-square"></div>
      <div class="brand-name">Harwick<br>Studio</div>
    </div>

    <div class="contact">
      <p class="contact-name">Harwick Studio</p>
      <address class="contact-address">4186 Maplecrest Rd. Unit B-2<br>Windsor, CO 80317</address>
      <p class="contact-web">www.harwickstudio-example.com<br>lu@harwickstudio-example.com</p>
    </div>
  </div>
</body>
</html>
```